Web Design - Personal Item Tags Portal

web page designs need to be created for a new company that provides item tracking tags and lets users register and report stolen/found items.
The theme of the designs needs to be energetic and convey a sense of freedom and adventure - where the user does not have to worry about their items since they have all been "tagged".
the client likes parts of the site at: http://www.plimcraft.example/
they like:
1. slider images at top of pages. large slider on front page. fixed smaller height picture on internal pages
2. fixed company message on left-hand-side
3. My Account button to be clear and stand out

other comments:
clean, simple
• brand focused
• will have clear call to actions
• will include a description of what and why
• will appeal to both males and females

sections that the website will have are:
Home
About Us
How it works
Why
Case Studies
Uses and Applications
Shop
Contact Us

please create 2 designs : 1 home page, 1 internal page

Final winner will also require HTML slicing to be done.

hi, i have now updated the images so they work. sorry!

Hi, looking at all the designs that are coming in, alot of them are great. Designers need to remember to make the register for an account button more prominent. Also, there should be a "report found" and "report lost" buttons on the front-page and should be prominent as well.

Thanks

Hi, the customer has come back with a few comments and modifications for the designs, if you are able to make some tweaks to your submissions, that will be great:

The client would like the designs to be modified to highlight 3 main actions:
1. Log In/Register
2. Find an Owner
3. Lost an Item

The home page shouldnt be too content heavy in terms of text, it should only have major highlight points of what the system does (the 3 points listed above). the inner page designs are OK to have more text though.

i will also upload some notes from the customer that can be used as a guide and also include the design styles which the customer likes (but is not entirely happy with).

uploaded image files (3) with customer feedback comments

```html
<!DOCTYPE html>
<html lang="en">
<head>
<meta charset="utf-8">
<title>Wayfind – Adventure First</title>
<link href="https://fonts.googleapis.com/css2?family=Anton&family=Questrial&family=Oswald:wght@300&family=Ubuntu+Condensed&display=swap" rel="stylesheet">
<style>
:root{
  --ink:#000;
  --brand-blue:#0a5a8c;
  --brand-blue-dark:#0b4a6e;
  --sky-blue:#1a9ad6;
  --ring:#5c503f;
  --white:#fff;
  --muted:#b5b5b5;
  --panel:rgba(45,38,30,.68);
  --hero-top:#8c9ba2;
  --hero-bottom:#cfb27a;
}
*{margin:0;padding:0;box-sizing:border-box}
html,body{width:1200px;height:1038px;overflow:hidden;background:var(--ink)}
.page{position:relative;width:1200px;height:1038px;background:var(--ink);font-family:Arial,Helvetica,sans-serif}
.abs{position:absolute}

/* header */
.header{left:0;top:0;width:1200px;height:154px;background:var(--ink)}
.brand-name{left:214px;top:28px;font-family:Questrial,sans-serif;font-size:46px;color:var(--white);line-height:1}
.brand-tagline{left:429px;top:50px;font-family:Questrial,sans-serif;font-size:20px;color:var(--white)}
.nav{left:184px;top:109px;width:1016px;height:45px;background:var(--brand-blue);border-top:1px solid #3d86b8}
.nav a{position:absolute;top:0;height:45px;line-height:45px;font-family:Questrial,sans-serif;font-size:20px;color:var(--white);text-decoration:none}
.nav a.active{background:#f2f2f2;color:var(--brand-blue);font-weight:bold;padding:0 14px;left:0}

/* hero */
.hero{left:0;top:154px;width:1200px;height:611px;overflow:hidden}
.hero-photo{left:0;top:0;width:1200px;height:611px;background:linear-gradient(180deg,var(--hero-top) 0%,var(--hero-bottom) 100%)}
.hero-title{left:0;width:662px;text-align:center;font-family:Anton,sans-serif;line-height:1}
.hero-title.accent{top:74px;font-size:59px;color:var(--brand-blue)}
.hero-title.main{top:134px;font-size:60px;color:#1c1c1c}
.action{width:200px;height:200px;border-radius:50%;background:var(--ring);padding:10px}
.action .face{width:180px;height:180px;border-radius:50%;border:7px solid var(--ink);background:var(--brand-blue);position:relative}
.action.primary .face{background:var(--ink)}
.action svg{position:absolute;left:50%;top:28px;transform:translateX(-50%)}
.action .label{position:absolute;left:0;right:0;top:108px;text-align:center;font-family:"Ubuntu Condensed",sans-serif;font-size:19px;color:var(--white)}
.about{left:27px;top:436px;width:617px;height:157px;border-radius:9px;background:var(--panel);padding:14px 42px 0 42px}
.about h2{font-family:Questrial,sans-serif;font-weight:bold;font-size:32px;color:var(--sky-blue);margin-left:2px}
.about p{margin-top:6px;font-size:14.3px;line-height:17.3px;color:var(--white)}
.dots{left:1032px;top:575px;display:flex;gap:12.5px}
.dots span{width:17px;height:17px;border-radius:50%;background:var(--ink)}
.dots span.on{background:var(--white)}
.hero-rule{left:0;top:763px;width:1200px;height:2px;background:var(--brand-blue)}

/* footer */
.footer h3{position:absolute;top:818px;font-family:Questrial,sans-serif;font-weight:normal;font-size:20px;letter-spacing:.5px;color:#d8d8d8}
.links{top:863px;list-style:none;font-size:14.5px;line-height:17.6px;color:var(--muted)}
.social{left:531px;top:851px;display:flex;gap:10px}
.social span{width:35px;height:35px;border-radius:50%;background:var(--brand-blue)}
.newsletter-label{left:531px;top:901px;font-size:13px;color:var(--muted)}
.email{left:529px;top:927px;width:226px;height:33px;border-radius:17px;background:var(--brand-blue-dark);padding-left:18px;line-height:33px;font-size:13px;color:#dfe8ee}
.subscribe{left:535px;top:973px;font-size:13.5px;font-weight:bold;color:#9a9a9a}
.phone{left:944px;top:846px;font-family:Oswald,sans-serif;font-weight:300;font-size:34px;color:#8a8a8a;line-height:1}
.copyright{left:925px;top:946px;width:200px;text-align:center;font-size:14.5px;line-height:17.6px;color:var(--muted)}
</style>
</head>
<body>
<div class="page">

  <header class="header abs">
    <div class="brand-name abs">Wayfind</div>
    <div class="brand-tagline abs">. . . adventure first</div>
    <nav class="nav abs">
      <a class="active" href="#">Home</a>
      <a href="#" style="left:104px">About us</a>
      <a href="#" style="left:218px">How it works</a>
      <a href="#" style="left:362px">Why</a>
      <a href="#" style="left:437px">Case Studies</a>
      <a href="#" style="left:586px">Uses and Applications</a>
      <a href="#" style="left:815px">Shop</a>
      <a href="#" style="left:897px">Contact Us</a>
    </nav>
  </header>

  <section class="hero abs">
    <div class="hero-photo abs" role="img" aria-label="Slider photo: a climber on a rock face at sunset"></div>
    <div class="hero-title accent abs">‘Adventure First’</div>
    <div class="hero-title main abs">Intrepid TAG Solutions</div>

    <a class="action primary abs" href="#" style="left:19px;top:220px">
      <div class="face">
        <svg width="70" height="74" viewBox="0 0 70 74"><circle cx="35" cy="20" r="18" fill="#fff"/><path d="M2 74 Q2 40 35 40 Q68 40 68 74 Z" fill="#fff"/></svg>
        <div class="label">Log In/Register</div>
      </div>
    </a>
    <a class="action abs" href="#" style="left:234px;top:220px">
      <div class="face">
        <svg width="90" height="74" viewBox="0 0 90 74"><rect x="4" y="2" width="82" height="52" rx="6" fill="#fff"/><rect x="11" y="9" width="68" height="38" fill="#0a5a8c"/><circle cx="30" cy="22" r="7" fill="none" stroke="#fff" stroke-width="3"/><line x1="35" y1="27" x2="44" y2="35" stroke="#fff" stroke-width="4"/><rect x="2" y="60" width="86" height="10" rx="3" fill="#fff"/></svg>
        <div class="label">Find an Owner</div>
      </div>
    </a>
    <a class="action abs" href="#" style="left:451px;top:220px">
      <div class="face">
        <svg width="90" height="74" viewBox="0 0 90 74"><rect x="14" y="0" width="48" height="74" rx="8" fill="#fff"/><rect x="20" y="9" width="36" height="52" fill="#0a5a8c"/><circle cx="38" cy="67" r="3" fill="#0a5a8c"/><path d="M44 30 L74 24 L86 38 L60 50 Z" fill="#fff" stroke="#0a5a8c" stroke-width="2"/><circle cx="52" cy="36" r="3" fill="#0a5a8c"/></svg>
        <div class="label">Lost an Item</div>
      </div>
    </a>

    <article class="about abs">
      <h2>About Wayfind</h2>
      <p>Nam liber tempor cum soluta nobis eleifend option congue nihil imperdiet doming id quod mazim placerat facer possim assum. Typi non habent claritatem insitam; est usus legentis in iis qui facit eorum claritatem. Investigationes demonstraverunt lectores legere me lius quod ii legunt saepius. Claritas est etiam processus .</p>
    </article>

    <div class="dots abs"><span></span><span class="on"></span><span></span><span></span><span></span></div>
  </section>
  <div class="hero-rule abs"></div>

  <footer class="footer">
    <h3 style="left:50px">NAVIGATION</h3>
    <ul class="links abs" style="left:50px">
      <li>Home</li><li>About us</li><li>How it works</li><li>Why</li><li>Case Studies</li><li>Uses and Applications</li><li>Shop</li>
    </ul>
    <ul class="links abs" style="left:249px">
      <li>Sitemap</li><li>Report Found</li><li>Report Lost</li><li>Register an Account</li><li>Contact Us</li><li>Terms of Use</li><li>Privacy Policy</li>
    </ul>

    <h3 style="left:533px">GET CONNECTED</h3>
    <div class="social abs"><span></span><span></span><span></span><span></span><span></span></div>
    <div class="newsletter-label abs">Subscribe to our newsletter</div>
    <div class="email abs">enter email address</div>
    <div class="subscribe abs">subscribe now&nbsp; ➤</div>

    <h3 style="left:945px">CONTACT US</h3>
    <div class="phone abs">0987 654 321</div>
    <div class="copyright abs">© Wayfind 2013.<br>All rights reserved.</div>
  </footer>

</div>
</body>
</html>
```